Dental Medical History Form - Content provided

Design a medical history form for a dental practice. Content is provided so all that is needed is the formatting to make it look great and easy to read.

"Patient Information" to include all information contained in top portion of the "Patient Medical History Form" docx file.

"Medical History" should follow the formatting and content of the "Exact Medical History" file as this is what the entry fields look like in our practice software and so we would like it to match.

1st page - Patient info, allergies, medications, antibiotics, joint replacement, pregnancy.

2nd page - Do you have, or have you had, any of the following? . . . . . . .

Target Market(s)

All ages but must be clear enough for elderly to read. Use as much space as possible to keep font size bigger yet keep to two pages

Industry/Entity Type

Dental

Font styles to use
Sans Serif

Requirements
Must have
• All content provided
• Our logo at the top (file provided)
• Century Gothic Font
• Limit to two pages

```html
<!DOCTYPE html>
<html lang="en">
<head>
<meta charset="utf-8">
<title>Medical History – Do you have, or have you had</title>
<link rel="stylesheet" href="https://fonts.googleapis.com/css2?family=Didact+Gothic&display=swap">
<style>
  :root {
    --page-bg: #f7f7f7;
    --panel-bg: #ffffff;
    --text: #454545;
    --heading: #2b2b2b;
    --box-border: #c4c4c4;
    --divider: #b5b5b5;
  }
  * { box-sizing: border-box; margin: 0; padding: 0; }
  html, body { width: 849px; height: 1200px; overflow: hidden; }
  body {
    position: relative;
    background: var(--page-bg);
    font-family: "Didact Gothic", "Century Gothic", sans-serif;
    color: var(--text);
  }
  .form-title, .form-thanks {
    position: absolute; left: 0; width: 849px; text-align: center;
    font-weight: 700; color: var(--heading);
  }
  .form-title { top: 51px; font-size: 13.6px; }
  .form-thanks { top: 1123px; font-size: 14.4px; }

  .panel { position: absolute; top: 90px; height: 1004px; background: var(--panel-bg); }
  .panel-left { left: 21px; width: 390px; }
  .panel-right { left: 450px; width: 379px; }
  .column-divider {
    position: absolute; left: 429px; top: 90px; height: 1004px;
    border-left: 1.5px dashed var(--divider);
  }

  .section { position: absolute; left: 0; width: 100%; }
  .section-heading {
    height: 19.8px; line-height: 19.8px; padding-left: var(--label-x);
    font-size: 12.4px; font-weight: 700; color: var(--heading); letter-spacing: .1px;
  }
  .row { position: relative; height: 19.8px; font-size: 13px; }
  .row-label { position: absolute; left: var(--label-x); top: 0; line-height: 19.8px; white-space: nowrap; }
  .row.tall { height: 34.4px; }
  .row.tall .row-label { line-height: 15.2px; top: 1px; }
  .choice { position: absolute; bottom: 2px; height: 16px; }
  .box { width: 21.6px; border: 1px solid var(--box-border); background: #fff; }
  .choice-text { line-height: 16px; }

  .panel-left  { --label-x: 13px; --b1: 255px; --t1: 285px; --b2: 314px; --t2: 346px; }
  .panel-right { --label-x: 40px; --b1: 236px; --t1: 264px; --b2: 292px; --t2: 322px; }
  .yes-box { left: var(--b1); } .yes-text { left: var(--t1); }
  .no-box  { left: var(--b2); } .no-text  { left: var(--t2); }

  .care-note {
    position: absolute; left: 34px; top: 1029px; width: 340px;
    font-size: 13px; line-height: 15.6px;
  }
  .field { position: absolute; left: 490px; width: 298.4px; border: 1px solid var(--box-border); background: #fff; }
  .field-label {
    position: absolute; left: 6px; font-size: 12.4px; font-weight: 700; color: var(--heading);
  }
  .other-heading { position: absolute; left: 497px; top: 813px; font-size: 12.4px; font-weight: 700; color: var(--heading); }
</style>
</head>
<body>

<h1 class="form-title">Do you have, or have you had, any of the following ?</h1>

<div class="panel panel-left"></div>
<div class="column-divider"></div>
<div class="panel panel-right"></div>

<div class="panel-left" style="position:absolute;left:21px;top:0;width:390px;height:1200px;">

  <section class="section" style="top:102.9px">
    <h2 class="section-heading">DENTAL</h2>
    <div class="row"><span class="row-label">Acid Reflux</span><span class="choice box yes-box"></span><span class="choice choice-text yes-text">Yes</span><span class="choice box no-box"></span><span class="choice choice-text no-text">No</span></div>
    <div class="row"><span class="row-label">Bad Breath/Taste</span><span class="choice box yes-box"></span><span class="choice choice-text yes-text">Yes</span><span class="choice box no-box"></span><span class="choice choice-text no-text">No</span></div>
    <div class="row"><span class="row-label">Bleeding/Swollen/Sore Gums</span><span class="choice box yes-box"></span><span class="choice choice-text yes-text">Yes</span><span class="choice box no-box"></span><span class="choice choice-text no-text">No</span></div>
    <div class="row"><span class="row-label">Blisters/Ulcers in Mouth</span><span class="choice box yes-box"></span><span class="choice choice-text yes-text">Yes</span><span class="choice box no-box"></span><span class="choice choice-text no-text">No</span></div>
    <div class="row"><span class="row-label">Broken tooth/filling</span><span class="choice box yes-box"></span><span class="choice choice-text yes-text">Yes</span><span class="choice box no-box"></span><span class="choice choice-text no-text">No</span></div>
    <div class="row"><span class="row-label">Burning tongue</span><span class="choice box yes-box"></span><span class="choice choice-text yes-text">Yes</span><span class="choice box no-box"></span><span class="choice choice-text no-text">No</span></div>
    <div class="row"><span class="row-label">Dry mouth</span><span class="choice box yes-box"></span><span class="choice choice-text yes-text">Yes</span><span class="choice box no-box"></span><span class="choice choice-text no-text">No</span></div>
    <div class="row"><span class="row-label">Food collection between teeth</span><span class="choice box yes-box"></span><span class="choice choice-text yes-text">Yes</span><span class="choice box no-box"></span><span class="choice choice-text no-text">No</span></div>
    <div class="row"><span class="row-label">Grinding/clenching teeth (day/night)</span><span class="choice box yes-box"></span><span class="choice choice-text yes-text">Yes</span><span class="choice box no-box"></span><span class="choice choice-text no-text">No</span></div>
    <div class="row"><span class="row-label">Loose teeth</span><span class="choice box yes-box"></span><span class="choice choice-text yes-text">Yes</span><span class="choice box no-box"></span><span class="choice choice-text no-text">No</span></div>
    <div class="row"><span class="row-label">Crooked teeth</span><span class="choice box yes-box"></span><span class="choice choice-text yes-text">Yes</span><span class="choice box no-box"></span><span class="choice choice-text no-text">No</span></div>
    <div class="row"><span class="row-label">Discoloured teeth</span><span class="choice box yes-box"></span><span class="choice choice-text yes-text">Yes</span><span class="choice box no-box"></span><span class="choice choice-text no-text">No</span></div>
    <div class="row"><span class="row-label">Sensitivity to Hot/Cold</span><span class="choice box yes-box"></span><span class="choice choice-text yes-text">Yes</span><span class="choice box no-box"></span><span class="choice choice-text no-text">No</span></div>
    <div class="row"><span class="row-label">Tooth pain when chewing</span><span class="choice box yes-box"></span><span class="choice choice-text yes-text">Yes</span><span class="choice box no-box"></span><span class="choice choice-text no-text">No</span></div>
    <div class="row"><span class="row-label">Jaw pain/Fracture</span><span class="choice box yes-box"></span><span class="choice choice-text yes-text">Yes</span><span class="choice box no-box"></span><span class="choice choice-text no-text">No</span></div>
    <div class="row"><span class="row-label">Orthodontic treatment/history</span><span class="choice box yes-box"></span><span class="choice choice-text yes-text">Yes</span><span class="choice box no-box"></span><span class="choice choice-text no-text">No</span></div>
    <div class="row"><span class="row-label">Oral Cancer</span><span class="choice box yes-box"></span><span class="choice choice-text yes-text">Yes</span><span class="choice box no-box"></span><span class="choice choice-text no-text">No</span></div>
  </section>

  <section class="section" style="top:478px">
    <h2 class="section-heading">DIET/LIFESTYLE</h2>
    <div class="row tall"><span class="row-label">Drink more than 1glass<br>alcohol per day</span><span class="choice box yes-box"></span><span class="choice choice-text yes-text">Yes</span><span class="choice box no-box"></span><span class="choice choice-text no-text">No</span></div>
    <div class="row"><span class="row-label">Smoking</span><span class="choice box yes-box"></span><span class="choice choice-text yes-text">Yes</span><span class="choice box no-box"></span><span class="choice choice-text no-text">No</span></div>
    <div class="row"><span class="row-label">Carbonated drinks</span><span class="choice box yes-box"></span><span class="choice choice-text yes-text">Yes</span><span class="choice box no-box"></span><span class="choice choice-text no-text">No</span></div>
    <div class="row"><span class="row-label">Sugary foods</span><span class="choice box yes-box"></span><span class="choice choice-text yes-text">Yes</span><span class="choice box no-box"></span><span class="choice choice-text no-text">No</span></div>
  </section>

  <section class="section" style="top:611.7px">
    <h2 class="section-heading">BLOOD</h2>
    <div class="row"><span class="row-label">Anaemia</span><span class="choice box yes-box"></span><span class="choice choice-text yes-text">Yes</span><span class="choice box no-box"></span><span class="choice choice-text no-text">No</span></div>
    <div class="row"><span class="row-label">Blood clots</span><span class="choice box yes-box"></span><span class="choice choice-text yes-text">Yes</span><span class="choice box no-box"></span><span class="choice choice-text no-text">No</span></div>
    <div class="row"><span class="row-label">Leukemia</span><span class="choice box yes-box"></span><span class="choice choice-text yes-text">Yes</span><span class="choice box no-box"></span><span class="choice choice-text no-text">No</span></div>
    <div class="row"><span class="row-label">Low platelets</span><span class="choice box yes-box"></span><span class="choice choice-text yes-text">Yes</span><span class="choice box no-box"></span><span class="choice choice-text no-text">No</span></div>
    <div class="row"><span class="row-label">Lymphoma</span><span class="choice box yes-box"></span><span class="choice choice-text yes-text">Yes</span><span class="choice box no-box"></span><span class="choice choice-text no-text">No</span></div>
  </section>

  <section class="section" style="top:750.9px">
    <h2 class="section-heading">CHEST</h2>
    <div class="row"><span class="row-label">Bronchitis</span><span class="choice box yes-box"></span><span class="choice choice-text yes-text">Yes</span><span class="choice box no-box"></span><span class="choice choice-text no-text">No</span></div>
    <div class="row"><span class="row-label">Cystic Fibrosis</span><span class="choice box yes-box"></span><span class="choice choice-text yes-text">Yes</span><span class="choice box no-box"></span><span class="choice choice-text no-text">No</span></div>
    <div class="row"><span class="row-label">Emphysema</span><span class="choice box yes-box"></span><span class="choice choice-text yes-text">Yes</span><span class="choice box no-box"></span><span class="choice choice-text no-text">No</span></div>
    <div class="row"><span class="row-label">Pneumonia</span><span class="choice box yes-box"></span><span class="choice choice-text yes-text">Yes</span><span class="choice box no-box"></span><span class="choice choice-text no-text">No</span></div>
  </section>

  <section class="section" style="top:870px">
    <h2 class="section-heading">INFECTIOUS DISEASE</h2>
    <div class="row"><span class="row-label">Creutzfeldt-Jakob Disease</span><span class="choice box yes-box"></span><span class="choice choice-text yes-text">Yes</span><span class="choice box no-box"></span><span class="choice choice-text no-text">No</span></div>
    <div class="row"><span class="row-label">Hepatitis A,B,C,D</span><span class="choice box yes-box"></span><span class="choice choice-text yes-text">Yes</span><span class="choice box no-box"></span><span class="choice choice-text no-text">No</span></div>
    <div class="row"><span class="row-label">HIV/AIDS</span><span class="choice box yes-box"></span><span class="choice choice-text yes-text">Yes</span><span class="choice box no-box"></span><span class="choice choice-text no-text">No</span></div>
    <div class="row"><span class="row-label">Influenza</span><span class="choice box yes-box"></span><span class="choice choice-text yes-text">Yes</span><span class="choice box no-box"></span><span class="choice choice-text no-text">No</span></div>
    <div class="row"><span class="row-label">Shingles</span><span class="choice box yes-box"></span><span class="choice choice-text yes-text">Yes</span><span class="choice box no-box"></span><span class="choice choice-text no-text">No</span></div>
    <div class="row"><span class="row-label">Tuberculosis</span><span class="choice box yes-box"></span><span class="choice choice-text yes-text">Yes</span><span class="choice box no-box"></span><span class="choice choice-text no-text">No</span></div>
  </section>

  <p class="care-note" style="left:13px">Oral health is linked to overall health and this comprehensive questionnaire will help us to provide you with optimal and safe care.</p>
</div>

<div class="panel-right" style="position:absolute;left:450px;top:0;width:379px;height:1200px;">

  <section class="section" style="top:102.9px">
    <h2 class="section-heading">HEART</h2>
    <div class="row"><span class="row-label">Angina</span><span class="choice box yes-box"></span><span class="choice choice-text yes-text">Yes</span><span class="choice box no-box"></span><span class="choice choice-text no-text">No</span></div>
    <div class="row"><span class="row-label">Atrial Fibrillation</span><span class="choice box yes-box"></span><span class="choice choice-text yes-text">Yes</span><span class="choice box no-box"></span><span class="choice choice-text no-text">No</span></div>
    <div class="row"><span class="row-label">Blood Pressure (High/Low)</span><span class="choice box yes-box"></span><span class="choice choice-text yes-text">Yes</span><span class="choice box no-box"></span><span class="choice choice-text no-text">No</span></div>
    <div class="row"><span class="row-label">Congenital Heart Disease</span><span class="choice box yes-box"></span><span class="choice choice-text yes-text">Yes</span><span class="choice box no-box"></span><span class="choice choice-text no-text">No</span></div>
    <div class="row"><span class="row-label">Heart attack</span><span class="choice box yes-box"></span><span class="choice choice-text yes-text">Yes</span><span class="choice box no-box"></span><span class="choice choice-text no-text">No</span></div>
    <div class="row"><span class="row-label">Heart murmur</span><span class="choice box yes-box"></span><span class="choice choice-text yes-text">Yes</span><span class="choice box no-box"></span><span class="choice choice-text no-text">No</span></div>
    <div class="row"><span class="row-label">Heart surgery</span><span class="choice box yes-box"></span><span class="choice choice-text yes-text">Yes</span><span class="choice box no-box"></span><span class="choice choice-text no-text">No</span></div>
    <div class="row"><span class="row-label">Heart valve replacement</span><span class="choice box yes-box"></span><span class="choice choice-text yes-text">Yes</span><span class="choice box no-box"></span><span class="choice choice-text no-text">No</span></div>
    <div class="row"><span class="row-label">Infective endocarditis</span><span class="choice box yes-box"></span><span class="choice choice-text yes-text">Yes</span><span class="choice box no-box"></span><span class="choice choice-text no-text">No</span></div>
    <div class="row"><span class="row-label">Rheumatic Heart Disease</span><span class="choice box yes-box"></span><span class="choice choice-text yes-text">Yes</span><span class="choice box no-box"></span><span class="choice choice-text no-text">No</span></div>
    <div class="row"><span class="row-label">Pacemaker</span><span class="choice box yes-box"></span><span class="choice choice-text yes-text">Yes</span><span class="choice box no-box"></span><span class="choice choice-text no-text">No</span></div>
    <div class="row"><span class="row-label">Stent</span><span class="choice box yes-box"></span><span class="choice choice-text yes-text">Yes</span><span class="choice box no-box"></span><span class="choice choice-text no-text">No</span></div>
  </section>

  <section class="section" style="top:381.3px">
    <h2 class="section-heading">OTHER</h2>
    <div class="row"><span class="row-label">Anxiety/PTSD</span><span class="choice box yes-box"></span><span class="choice choice-text yes-text">Yes</span><span class="choice box no-box"></span><span class="choice choice-text no-text">No</span></div>
    <div class="row"><span class="row-label">Arthritis</span><span class="choice box yes-box"></span><span class="choice choice-text yes-text">Yes</span><span class="choice box no-box"></span><span class="choice choice-text no-text">No</span></div>
    <div class="row"><span class="row-label">Alzheimer's</span><span class="choice box yes-box"></span><span class="choice choice-text yes-text">Yes</span><span class="choice box no-box"></span><span class="choice choice-text no-text">No</span></div>
    <div class="row"><span class="row-label">Asthma</span><span class="choice box yes-box"></span><span class="choice choice-text yes-text">Yes</span><span class="choice box no-box"></span><span class="choice choice-text no-text">No</span></div>
    <div class="row"><span class="row-label">Anaphylaxis</span><span class="choice box yes-box"></span><span class="choice choice-text yes-text">Yes</span><span class="choice box no-box"></span><span class="choice choice-text no-text">No</span></div>
    <div class="row"><span class="row-label">Auto-immune disease</span><span class="choice box yes-box"></span><span class="choice choice-text yes-text">Yes</span><span class="choice box no-box"></span><span class="choice choice-text no-text">No</span></div>
    <div class="row"><span class="row-label">Coeliac</span><span class="choice box yes-box"></span><span class="choice choice-text yes-text">Yes</span><span class="choice box no-box"></span><span class="choice choice-text no-text">No</span></div>
    <div class="row"><span class="row-label">Depression</span><span class="choice box yes-box"></span><span class="choice choice-text yes-text">Yes</span><span class="choice box no-box"></span><span class="choice choice-text no-text">No</span></div>
    <div class="row"><span class="row-label">Diabetes</span><span class="choice box yes-box"></span><span class="choice choice-text yes-text">Yes</span><span class="choice box no-box"></span><span class="choice choice-text no-text">No</span></div>
    <div class="row"><span class="row-label">Epilepsy</span><span class="choice box yes-box"></span><span class="choice choice-text yes-text">Yes</span><span class="choice box no-box"></span><span class="choice choice-text no-text">No</span></div>
    <div class="row"><span class="row-label">Kidney Disease</span><span class="choice box yes-box"></span><span class="choice choice-text yes-text">Yes</span><span class="choice box no-box"></span><span class="choice choice-text no-text">No</span></div>
    <div class="row"><span class="row-label">Liver Disease</span><span class="choice box yes-box"></span><span class="choice choice-text yes-text">Yes</span><span class="choice box no-box"></span><span class="choice choice-text no-text">No</span></div>
    <div class="row"><span class="row-label">Osteoporosis</span><span class="choice box yes-box"></span><span class="choice choice-text yes-text">Yes</span><span class="choice box no-box"></span><span class="choice choice-text no-text">No</span></div>
    <div class="row"><span class="row-label">Parkinson's</span><span class="choice box yes-box"></span><span class="choice choice-text yes-text">Yes</span><span class="choice box no-box"></span><span class="choice choice-text no-text">No</span></div>
    <div class="row"><span class="row-label">Radiation to Head/Neck</span><span class="choice box yes-box"></span><span class="choice choice-text yes-text">Yes</span><span class="choice box no-box"></span><span class="choice choice-text no-text">No</span></div>
    <div class="row"><span class="row-label">Schizophrenia</span><span class="choice box yes-box"></span><span class="choice choice-text yes-text">Yes</span><span class="choice box no-box"></span><span class="choice choice-text no-text">No</span></div>
    <div class="row"><span class="row-label">Snoring</span><span class="choice box yes-box"></span><span class="choice choice-text yes-text">Yes</span><span class="choice box no-box"></span><span class="choice choice-text no-text">No</span></div>
    <div class="row"><span class="row-label">Sleep apnea</span><span class="choice box yes-box"></span><span class="choice choice-text yes-text">Yes</span><span class="choice box no-box"></span><span class="choice choice-text no-text">No</span></div>
    <div class="row"><span class="row-label">Stroke</span><span class="choice box yes-box"></span><span class="choice choice-text yes-text">Yes</span><span class="choice box no-box"></span><span class="choice choice-text no-text">No</span></div>
  </section>
</div>

<h2 class="other-heading">OTHER</h2>
<div class="field" style="top:832px;height:22.4px"></div>
<div class="field" style="top:864px;height:22.4px"></div>
<div class="field" style="top:897.6px;height:22.4px"></div>

<div class="field" style="top:963px;height:70.4px"><span class="field-label" style="top:9px">SIGNATURE</span></div>
<div class="field" style="top:1043px;height:23.4px"><span class="field-label" style="top:4px">Date:</span></div>

<p class="form-thanks">Thank you for the time to complete your medical history form.</p>

</body>
</html>
```